Bellwin, Horup & Bellwin Concussion Infographic

We need an infographic for a Bellwin, Horup & Bellwin, a personal injury law firm based in Florida. Our goal is to raise awareness about concussions targeted towards young teens. We have researched and gathered info on the symptoms, danger signs, what to do and not do after sustaining a concussion, and additional facts on the severity of concussions. Our main goal for this infographic is to create a well-designed, easy-to-read infographic that is visually appealing. The more graphics we can use to aid with the statistics we are offering, the better. What we don't want is just an infographic with a bunch of facts listed without any visual aids. We need a creative way to capture the audiences attention through eye-catching visuals so they will be enticed to read the statistics in the infographic.

Target Market(s)

high school sports teams, youth sports leagues,

Industry/Entity Type

Legal

Font styles to use
Serif

Colors
0355a3
33a6d7
ffffff
fece3e

Requirements
Must have
• Visual aids that compliment our stats, visually appealing imagery, cite our sources at the bottom of the infographic in fine print
Nice to have
• creative and visual ways to back up statistics, contains a flow both cognitively and visually - like a good story, conveying a message at a glance - taking alot of data and boiling it down to one image,
Should not have
• any pictures or visuals that may scare or turn off audience,

```html
<!DOCTYPE html>
<html lang="en">
<head>
<meta charset="utf-8">
<title>Concussions! – Bellwin, Horup &amp; Bellwin</title>
<link rel="stylesheet" href="https://fonts.googleapis.com/css2?family=Archivo+Black&family=Ubuntu:ital,wght@0,400;0,500;0,700;1,400&display=swap">
<style>
  :root{
    --navy:#0b55a3;
    --sky:#33a6d7;
    --sun:#fece3e;
    --white:#ffffff;
    --alert:#c01f2e;
    --ink:#111111;
    --mist:#e2e2e2;
    --skin:#e9c9a0;
  }
  *{box-sizing:border-box;margin:0;padding:0}
  html,body{width:1200px;height:1200px;overflow:hidden;background:var(--white)}
  body{font-family:"Ubuntu",sans-serif;color:var(--white)}
  .canvas{position:relative;width:1200px;height:1200px;overflow:hidden;background:var(--white)}
  .abs{position:absolute}

  .title-band{left:0;top:0;width:1200px;height:74px;background:var(--navy);
    display:flex;align-items:center;justify-content:center}
  .title-band h1{font-family:"Archivo Black",sans-serif;font-size:62px;letter-spacing:1px;color:var(--white);line-height:1}

  .backdrop{left:36px;top:140px;width:1150px;height:910px;
    border-radius:46% 50% 44% 48% / 52% 48% 46% 50%;
    background:var(--mist);opacity:.7}

  .burst{left:0;top:76px;width:480px;height:380px}

  .tab{background:var(--sky);color:var(--white);
    display:flex;align-items:center;justify-content:center;text-align:center;
    text-shadow:1px 2px 2px rgba(0,0,0,.4);border-radius:12px;
    box-shadow:3px 4px 6px rgba(0,0,0,.25);line-height:1.12}
  .tab.left{border-radius:0 12px 12px 0;justify-content:flex-start;padding-left:18px}
  .tab h2{font-size:24px;font-weight:700;letter-spacing:-.2px}

  .card{background:var(--navy);color:var(--white);border-radius:12px;font-size:9.6px;line-height:1.3}

  .illus{border-radius:12px}

  .definition{left:244px;top:146px;width:228px;height:71px;padding:12px 10px;text-align:justify}
  .note{left:76px;top:332px;width:296px;height:34px;border-radius:18px;padding:6px 10px 0 52px;font-size:7.6px}
  .note-icon{left:74px;top:332px;width:50px;height:40px}

  .stat-circle{border-radius:50%;display:flex;align-items:center;justify-content:center;text-align:center}
  .stat-black{left:477px;top:320px;width:88px;height:88px;background:var(--ink);font-weight:700;font-size:15px;line-height:1.15;z-index:2}
  .stat-red{left:477px;top:465px;width:88px;height:88px;background:var(--alert);font-size:56px;font-weight:700;z-index:2}
  .stat-one{left:548px;top:340px;width:222px;height:48px;padding:12px 8px 0 22px;text-align:justify}
  .stat-two{left:436px;top:412px;width:228px;height:46px;padding:11px 10px}
  .stat-three{left:548px;top:470px;width:222px;height:76px;padding:9px 8px 0 22px;text-align:justify}
  .crowd{left:666px;top:392px;width:96px;height:74px;border-radius:4px;
    background:linear-gradient(180deg,#3a3a3a,#222)}

  .list{list-style:none}
  .symptoms{left:854px;top:192px;width:290px;height:80px;padding:11px 10px;border-radius:16px}
  .danger{left:830px;top:600px;width:346px;height:102px;padding:11px 10px;border-radius:12px 0 12px 12px}
  .danger li{margin-bottom:11px}
  .danger em{font-size:7px}

  .todo{left:24px;top:694px;width:638px;height:202px;padding:12px 16px 0 16px;font-size:9.2px}
  .todo ol{list-style:none}
  .todo li{margin-bottom:11px;padding-left:12px;text-indent:-12px}
  .todo .sub{display:block;padding-left:24px;text-indent:0}
  .todo .sub i{display:block;margin-left:-16px}

  .avoid{left:830px;top:854px;width:346px;height:132px;padding:12px 10px}
  .avoid li{margin-bottom:10px}
  .avoid b{font-weight:700;display:block}
  .avoid span{display:block;padding-left:8px}

  .extra{left:198px;top:1064px;width:804px;height:68px;padding:14px 10px;font-size:9.4px}
  .extra li{margin-bottom:12px}

  .sources{left:0;top:1158px;width:1000px;height:42px;background:var(--sun);color:#333;font-size:8.6px;
    display:grid;grid-template-columns:28px 490px 28px 1fr;padding:7px 0 0 24px;row-gap:2px;line-height:1.3}

  .firm{left:1020px;top:1132px;width:170px;height:44px;display:flex;align-items:center;justify-content:center;
    font-family:"Ubuntu",sans-serif;font-weight:500;font-size:15px;color:var(--ink);text-align:center;line-height:1.05}
</style>
</head>
<body>
<div class="canvas">

  <header class="abs title-band"><h1>CONCUSSIONS !</h1></header>

  <div class="abs backdrop" role="img" aria-label="Large light grey line drawing of a brain filling the background"></div>

  <svg class="abs burst" viewBox="0 0 480 380" aria-hidden="true">
    <polygon fill="var(--sun)" points="0,20 300,30 400,22 280,90 250,180 330,320 330,345 190,260 90,330 40,300 0,300"/>
  </svg>

  <div class="abs tab left" style="left:0;top:76px;width:316px;height:60px"><h2>What is a Concussion??!</h2></div>

  <div class="abs illus" role="img" aria-label="Cartoon boy hit on the head by a soccer ball, brain visible"
       style="left:40px;top:120px;width:200px;height:200px;background:radial-gradient(circle at 50% 50%,#f3e4cf,#e9c9a0 55%,rgba(254,206,62,0) 72%)"></div>

  <p class="abs card definition">A concussion is a type of traumatic brain injury caused by a bump, jolt, or blow to the head or body which causes the brain to jerk back and forth rapidly inside the skull.</p>

  <p class="abs card note">More than 90% of sport-related concussions occur WITHOUT the person losing consciousness or being "knocked out."*</p>
  <svg class="abs note-icon" viewBox="0 0 50 40" aria-hidden="true">
    <path d="M25 2 A23 17 0 1 1 14 34 L4 40 L10 30 A23 17 0 0 1 25 2Z" fill="var(--ink)"/>
    <text x="24" y="28" fill="var(--white)" font-family="Georgia,serif" font-style="italic" font-weight="700" font-size="22" text-anchor="middle">i</text>
  </svg>

  <div class="abs tab" style="left:424px;top:238px;width:352px;height:86px"><h2>How Often do People Sustain<br>Concussions From Sports?</h2></div>

  <p class="abs card stat-one">people are involved in a sport-related concussion each year.</p>
  <div class="abs stat-circle stat-black">1.6 to 3.8<br>million</div>

  <p class="abs card stat-two">High school athletes sustained an estimated of 300,000 concussions per year.</p>
  <div class="abs crowd" role="img" aria-label="Rows of small people figures representing athletes"></div>

  <p class="abs card stat-three">An athlete who has suffered from a concussion in the past, is 3-6 times more likely to suffer from another concussion compared to an athlete who has never had one.</p>
  <div class="abs stat-circle stat-red">!</div>

  <div class="abs tab" style="left:824px;top:104px;width:352px;height:58px"><h2>Symptoms Reported by Athlete</h2></div>
  <ul class="abs card list symptoms">
    <li>• Headache or "pressure" in head</li>
    <li>• Problems with balance or dizziness</li>
    <li>• Confusion, trouble with concentration or memory problems</li>
    <li>• Feeling hazy, sluggish, foggy, or groggy</li>
    <li>• Nauseau or vomiting</li>
  </ul>
  <div class="abs illus" role="img" aria-label="Cartoon boy looking dizzy with stars around his head"
       style="left:952px;top:276px;width:216px;height:150px;background:radial-gradient(circle at 55% 50%,#e2bf95 0%,#e9c9a0 40%,rgba(226,226,226,0) 70%)"></div>

  <div class="abs tab" style="left:824px;top:516px;width:352px;height:58px"><h2>Danger Signs !</h2></div>
  <div class="abs illus" role="img" aria-label="Cartoon blond boy with wide eyes"
       style="left:704px;top:568px;width:132px;height:108px;background:radial-gradient(circle at 50% 50%,#e9c9a0 0%,#f2cd58 55%,rgba(226,226,226,0) 72%)"></div>
  <ul class="abs card list danger">
    <li>• One pupil <em>(the black circular part in the middle of the eye)</em> larger than the other</li>
    <li>• A headache that gets worse and does not go away</li>
    <li>• Loss of consciousness of more than a minute</li>
    <li>• Drowsiness or cannot be awakened</li>
  </ul>
  <div class="abs illus" role="img" aria-label="Red wall clock showing the time"
       style="left:1088px;top:629px;width:96px;height:96px;border-radius:50%;
       background:radial-gradient(circle at 50% 50%,#f4f4f4 0%,#f4f4f4 58%,var(--alert) 66%,var(--alert) 100%)"></div>

  <div class="abs tab" style="left:24px;top:610px;width:638px;height:58px"><h2>What to Do After Sustaining a Concussion</h2></div>
  <div class="abs card todo">
    <ol>
      <li>1) Remove Athlete from Play. Pay attention to any signs or symptoms of a concussion and keep athlete out of game when in doubt.</li>
      <li>2) Seek Medical Attention. Ensure that the athlete is evaluated by a health care professional.
        <span class="sub"><i>(Record the following information that may assist the health care professional):</i>
        - cause of the injury and impact of the hit or blow to the head or body.<br>
        - any loss of consciousness, and if so, for how long.<br>
        - any memory loss right after the injury.<br>
        - number of previous concussions if any.</span></li>
      <li>3) Rest. After a concussion the brain needs time to heal. This means avoiding activities that are physically demanding or require alot of concentration, which can slow your recovery or worsen your symptoms.</li>
      <li>4) Inform and Educate Parents. It is important for the parents to speak with their health care professional as well as their kids to learn about all the symptoms of concussions, the proper steps to take in treating the injury, the potential long-term effects of concussions and the dangers of returing too soon to physically and mentally demanding activities.</li>
    </ol>
  </div>
  <div class="abs illus" role="img" aria-label="Red medical cross with a stethoscope"
       style="left:516px;top:716px;width:180px;height:120px;background:radial-gradient(ellipse at 35% 45%,var(--alert) 0%,rgba(192,31,46,.55) 35%,rgba(11,85,163,0) 65%)"></div>

  <div class="abs tab" style="left:824px;top:770px;width:352px;height:58px"><h2>What Not to Do After a<br>Concussion</h2></div>
  <ul class="abs card list avoid">
    <li><b>• Physical Activity</b><span>An activity that causes an increase in heart rate may worsen symptoms.</span></li>
    <li><b>• Strenuous Mental Activities</b><span>Such as computer work, reading, playing video games and watching TV.</span></li>
    <li><b>• Driving</b><span>Do not drive for at least 24 hours the injury. Reaction time may be slowed down which can increase the risk of accidents.</span></li>
  </ul>
  <div class="abs illus" role="img" aria-label="Red video game controller"
       style="left:744px;top:880px;width:92px;height:76px;background:radial-gradient(ellipse at 50% 50%,var(--alert) 0%,rgba(192,31,46,.7) 45%,rgba(226,226,226,0) 72%)"></div>

  <div class="abs tab" style="left:422px;top:992px;width:352px;height:56px"><h2>Additional Information</h2></div>
  <ul class="abs card list extra">
    <li>• Teens generally require a longer recovery time than adults for concussions because their brains are still developing.</li>
    <li>• Research indicates that 80-90% of concussions will resolve within 7-10 days, however depending on the person and severity of the concussion, may take much longer</li>
  </ul>

  <footer class="abs sources">
    <span>*</span><span>Northfield Health</span>
    <span>†</span><span>http://headsafe-facts.org/concussions-101/statistics/</span>
    <span>**</span><span>National Office for Youth Health and Injury Prevention</span>
    <span>‡</span><span>https://health.lakeviewclinic-example.org/2012/08/suspect-a-concussion-what-you-need-to-know/</span>
  </footer>

  <div class="abs firm">Bellwin, Horup<br>&amp; Bellwin</div>

</div>
</body>
</html>
```